Magical healing ointment looking for new branded labels

I need a new product label for my healing comfrey ointments, which started as just a simple ointment, and has grown to include a few varients including a body oil and lip balm. It sells quite well when I have a market, which I don't always have time to do - so I'd like to take it and leave it with some health shops, however for this I'd really like a more professional label to take these products further.

The company name is Brightwren Meadow - slogan Gathered with Care; as I am both a healer that makes ointments and yet also make scarves, cowls with high quality natural wool.
The ointment is simply called 'Comfrey Ointment', don't mind if it has Magical or healing in front of it. It's made by me, with high quality all natural, locally sourced organic ingredients, and supports the healing of bones, injuries, RSI, arthritis, rheuma, eczema, aches and pains.. Comfrey itself is an ancient herb also used in medieval herblore and by the ancient romans, so my keys words are to get feeling for the brand:
Timeless/ classic/ clean/ natural/ quality/ confident/ healing

I would like the labels to stand out, and look professional. The smallest size is 6 x 2.5 cm, this is an amber small jar of 30ml, the larger jar is double that size at 60ml, and the bottles bigger. I would like to be able to add a bit on the side if needed to add ingredients, and be able to scale the label up or down depending on the size of the jar. On top of this would like to be able to text as needed depending on the product in the jar.

Have included my company logo - for an idea of what that looks like, please note though that this branding or style doesn't need to include this logo, nor look like this logo. I've also included an example of someone who I think is doing a good job of being unique, simple, classic and appealing. Let me know if you have any questions. Thanks!

Target Market(s)

People with an eco-sustainable mind-set that are looking to resolve ailments naturally.

Industry/Entity Type

Health

Requirements
Must have
• The product name, and company name
Nice to have
• I'd like to leave most of the design to the designers ideas, however am ok to have leaves - or natural elements that support the typography, but not overwhelm it.

```html
<!DOCTYPE html>
<html lang="en">
<head>
<meta charset="utf-8">
<title>Brightwren Meadow – Comfrey Ointment Label</title>
<link rel="stylesheet" href="https://fonts.googleapis.com/css2?family=Delius&family=Architects+Daughter&family=Open+Sans:wght@700&display=swap">
<style>
  :root {
    --page-bg: #ffffff;
    --ink: #111111;
    --label-light: #ffffff;
    --label-mid: #d9d9d9;
    --label-edge: #8c8c8c;
    --tag-bg: #111111;
    --tag-text: #ffffff;
  }
  html, body {
    margin: 0;
    padding: 0;
    width: 1200px;
    height: 1000px;
    overflow: hidden;
    background: var(--page-bg);
  }
  .canvas {
    position: relative;
    width: 1200px;
    height: 1000px;
    display: flex;
    align-items: center;
    justify-content: center;
  }
  .label {
    position: relative;
    width: 960px;
    height: 660px;
    background: linear-gradient(90deg,
      var(--label-edge) 0%,
      var(--label-mid) 18%,
      var(--label-light) 40%,
      var(--label-light) 60%,
      var(--label-mid) 82%,
      var(--label-edge) 100%);
    color: var(--ink);
    display: flex;
    flex-direction: column;
    align-items: center;
    box-sizing: border-box;
    padding-top: 60px;
  }
  .brand-name {
    font-family: "Delius", cursive;
    font-size: 48px;
    line-height: 1.1;
    margin: 0;
    color: var(--ink);
  }
  .brand-tagline {
    font-family: "Delius", cursive;
    font-size: 24px;
    line-height: 1.2;
    margin: 8px 0 0;
    color: var(--ink);
  }
  .product-title {
    display: flex;
    align-items: center;
    gap: 10px;
    margin-top: 26px;
  }
  .product-name {
    font-family: "Delius", cursive;
    font-size: 112px;
    line-height: 1.05;
    letter-spacing: 2px;
    margin: 0;
    font-weight: 400;
  }
  .plus-icon { width: 44px; height: 44px; }
  .product-type {
    font-family: "Delius", cursive;
    font-size: 82px;
    line-height: 1;
    margin: 0;
  }
  .benefits {
    font-family: "Architects Daughter", cursive;
    font-size: 24px;
    line-height: 1.4;
    text-align: center;
    margin: 32px 0 0;
  }
  .benefits .intro { display: block; font-size: 19px; }
  .net-weight {
    margin-top: 22px;
    background: var(--tag-bg);
    color: var(--tag-text);
    font-family: "Open Sans", sans-serif;
    font-weight: 700;
    font-size: 24px;
    line-height: 1.3;
    padding: 6px 18px;
  }
</style>
</head>
<body>
  <main class="canvas">
    <section class="label">
      <p class="brand-name">Brightwren Meadow</p>
      <p class="brand-tagline">Gathered with Care</p>

      <div class="product-title">
        <svg class="plus-icon" viewBox="0 0 48 48" aria-hidden="true">
          <rect x="18" y="4" width="12" height="40" fill="var(--ink)"/>
          <rect x="4" y="18" width="40" height="12" fill="var(--ink)"/>
        </svg>
        <h1 class="product-name">COMFREY</h1>
        <svg class="plus-icon" viewBox="0 0 48 48" aria-hidden="true">
          <rect x="18" y="4" width="12" height="40" fill="var(--ink)"/>
          <rect x="4" y="18" width="40" height="12" fill="var(--ink)"/>
        </svg>
      </div>
      <p class="product-type">ointment</p>

      <p class="benefits">
        <span class="intro">SUPPORTS THE HEALING OF :</span>
        Bones, Injuries, RSI, Arthritis,<br>
        Rheuma, Eczema, Aches and Pains.
      </p>

      <div class="net-weight">Net. Wt. 1 oz.</div>
    </section>
  </main>
</body>
</html>
```